Holiday Rental Company Flyer Design (DL not A5)

Note from PixelFolk Administration: The category sizing selected is A5, however the project requires DL sized artwork. Please refer to the DL template link below while the 'Special Requirements' are updated accordingly.

Project Brief:
We need a double sided DL flyer designed for an up market Holiday Rental Company that portrays a personalised approach to property management. These are to be used for letter box drops to homes we're specifically targeting so the design should be modern, complimentary colour palette, uncluttered & visually appealing.

Please Download the DL Template from Quillmark here: http://www.quillmark.com.au/qm/ns/propath/UploadResources.aspx?selectedTab=0?pfid=BFB&pf_id=BFB&xnav=easypath-upload-image#Templates

Target Market(s)

Wealthy Home Owners

Industry/Entity Type

It Company

Font styles to use
Other font styles liked:
• Avant Garde Extra Light & Demi

Colors
33b8a4

Requirements
Must have
• DL Flyer sizes (210mm width x 99mm width, plus 3mm bleed)
• Front: Logo, Main Image & Grab
• Back: Contact Details & Brief Description of our business
• Images: Ideally the main image should be the house with the pool but alternatively a lifestyle images could also be used.
Nice to have
• A creative designer!
Should not have
• Clutter & busy designs

```html
<!DOCTYPE html>
<html lang="en">
<head>
<meta charset="utf-8">
<title>Harbour Retreats – DL Flyer Concept 1</title>
<link rel="stylesheet" href="https://fonts.googleapis.com/css2?family=Questrial&family=Mulish:wght@400;500&display=swap">
<style>
  :root {
    --teal: #06b394;
    --teal-light: #84d4c6;
    --charcoal: #231f20;
    --ink: #111111;
    --white: #ffffff;
    --page: #ffffff;
    --card-border: #cfcfcf;
    --dusk-1: #2a2b6b;
    --dusk-2: #6b5aa8;
    --dusk-3: #c89a55;
  }
  * { box-sizing: border-box; margin: 0; padding: 0; }
  html, body { width: 1200px; height: 1000px; overflow: hidden; background: var(--page); }
  body { position: relative; font-family: "Mulish", Arial, sans-serif; color: var(--ink); }

  .concept-title {
    position: absolute; top: 36px; left: 0; width: 1200px; text-align: center;
    font-family: "Questrial", sans-serif; font-size: 29px; letter-spacing: 0.5px;
  }
  .side-label {
    position: absolute; font-family: "Questrial", sans-serif; font-size: 27px;
    transform: rotate(-90deg); transform-origin: center; width: 160px; text-align: center;
  }
  .side-label--front { left: 48px; top: 283px; }
  .side-label--back { left: 48px; top: 732px; }

  .flyer { position: absolute; left: 180px; width: 833px; overflow: hidden; }
  .flyer--front { top: 90px; height: 415px; }
  .flyer--back { top: 549px; height: 417px; border: 1px solid var(--card-border); background: var(--white); }
  .flyer svg.shapes { position: absolute; inset: 0; }

  .hero-photo {
    position: absolute; inset: 0;
    background: linear-gradient(110deg, var(--dusk-3) 0%, #5a4a7a 30%, var(--dusk-2) 55%, var(--dusk-1) 100%);
  }
  .grab-band {
    position: absolute; left: 0; top: 23px; width: 620px; height: 52px;
    background: linear-gradient(90deg, rgba(255,255,255,0.85) 0%, rgba(255,255,255,0.75) 70%, rgba(255,255,255,0) 100%);
    font-family: "Questrial", sans-serif; font-size: 19px; letter-spacing: 0.3px;
    line-height: 52px; padding-left: 21px; color: var(--ink);
  }
  .brand {
    position: absolute; font-family: "Questrial", sans-serif; color: var(--white);
    letter-spacing: 2px; line-height: 1.05; text-align: center;
  }
  .brand--front { left: 600px; top: 272px; width: 210px; font-size: 31px; }
  .brand--back { left: 690px; top: 335px; width: 130px; font-size: 19px; }

  .intro { position: absolute; left: 23px; top: 36px; width: 470px; }
  .intro h2 { font-weight: 400; font-size: 27px; margin-bottom: 12px; }
  .intro h2 .accent { color: var(--teal); font-weight: 500; }
  .intro p { font-size: 14.5px; line-height: 24px; margin-bottom: 14px; }

  .contact-photo {
    position: absolute; left: 23px; top: 231px; width: 144px; height: 136px;
    background: linear-gradient(160deg, #d9c8ad 0%, #c9b14a 45%, #d8d2cc 100%);
  }
  .contact-box {
    position: absolute; left: 177px; top: 231px; width: 314px; height: 136px;
    background: var(--teal); color: var(--white); padding: 12px 0 0 20px;
  }
  .contact-row { display: flex; align-items: center; gap: 12px; font-size: 14.5px; height: 25px; }
  .contact-row svg { width: 17px; height: 17px; flex: none; }
  .contact-row--phone { font-size: 22px; height: 28px; }

  .services { position: absolute; left: 522px; top: 28px; width: 300px; color: var(--white); }
  .services p { font-size: 14.5px; line-height: 24px; margin-bottom: 22px; }
  .services ul { list-style: none; }
  .services li { display: flex; gap: 10px; font-size: 13px; line-height: 20px; margin-bottom: 17px; }
  .services li svg { width: 15px; height: 12px; flex: none; margin-top: 4px; }
</style>
</head>
<body>
  <h1 class="concept-title">CONCEPT 1</h1>
  <div class="side-label side-label--front">FRONT</div>
  <div class="side-label side-label--back">BACK</div>

  <section class="flyer flyer--front">
    <div class="hero-photo" role="img" aria-label="Photo of a modern holiday home at dusk with a lit swimming pool"></div>
    <svg class="shapes" width="833" height="415" viewBox="0 0 833 415">
      <defs>
        <linearGradient id="frontTeal" x1="0" y1="0" x2="0" y2="1">
          <stop offset="0" stop-color="#84d4c6"/>
          <stop offset="1" stop-color="#06b394"/>
        </linearGradient>
      </defs>
      <path d="M20,415 C320,395 660,250 833,0 L833,415 Z" fill="url(#frontTeal)"/>
      <path d="M20,415 C320,395 660,250 833,0" fill="none" stroke="#ffffff" stroke-width="2"/>
      <circle cx="397" cy="308" r="64" fill="#a9b9c4" stroke="#ffffff" stroke-width="3" role="img" aria-label="Photo of a small sailing boat on calm water"/>
      <circle cx="556" cy="224" r="58" fill="#c3b36a" stroke="#ffffff" stroke-width="3" role="img" aria-label="Photo of yellow cushions on a bed"/>
      <circle cx="691" cy="135" r="57" fill="#37b7c4" stroke="#ffffff" stroke-width="3" role="img" aria-label="Photo of seals swimming in turquoise water"/>
    </svg>
    <div class="grab-band">HOLIDAY RENTAL MANAGEMENT WITH A DIFFERENCE</div>
    <div class="brand brand--front">HARBOUR<br>RETREATS</div>
  </section>

  <section class="flyer flyer--back">
    <svg class="shapes" width="833" height="417" viewBox="0 0 833 417">
      <defs>
        <linearGradient id="backTeal" x1="0" y1="0" x2="0" y2="1">
          <stop offset="0" stop-color="#84d4c6"/>
          <stop offset="1" stop-color="#06b394"/>
        </linearGradient>
      </defs>
      <path d="M506,0 H833 V222 C740,300 630,360 506,385 Z" fill="var(--charcoal)"/>
      <path d="M270,417 C520,405 720,330 833,222 L833,417 Z" fill="url(#backTeal)"/>
      <path d="M270,417 C520,405 720,330 833,222" fill="none" stroke="#ffffff" stroke-width="2"/>
    </svg>

    <div class="intro">
      <h2>What we do <span class="accent">differently!</span></h2>
      <p>Rather than relying upon a key safe or a central pick-up destination, a ‘Harbour Retreats’ staff member will greet guests upon arrival.</p>
      <p>If you’d like to know what your property could achieve or require additional information, please contact us on:</p>
    </div>

    <div class="contact-photo" role="img" aria-label="Photo of yellow cushions on a bed with a colourful quilt"></div>
    <div class="contact-box">
      <div class="contact-row contact-row--phone">
        <svg viewBox="0 0 24 24"><path d="M6.6 10.8a15 15 0 0 0 6.6 6.6l2.2-2.2a1 1 0 0 1 1-.25 11.4 11.4 0 0 0 3.6.6 1 1 0 0 1 1 1V20a1 1 0 0 1-1 1A17 17 0 0 1 3 4a1 1 0 0 1 1-1h3.5a1 1 0 0 1 1 1c0 1.25.2 2.45.6 3.6a1 1 0 0 1-.25 1z" fill="#fff"/></svg>
        <span>(03)5120 4417</span>
      </div>
      <div class="contact-row">
        <svg viewBox="0 0 24 24"><path d="M12 2a6 6 0 0 0-6 6c0 4.5 6 10 6 10s6-5.5 6-10a6 6 0 0 0-6-6zm0 8.2A2.2 2.2 0 1 1 12 5.8a2.2 2.2 0 0 1 0 4.4z" fill="#fff"/><path d="M3 22h18" stroke="#fff" stroke-width="2"/></svg>
        <span>PO Box 48, Glenmere Victoria 3950</span>
      </div>
      <div class="contact-row">
        <svg viewBox="0 0 24 24"><rect x="2" y="5" width="20" height="14" fill="#fff"/><path d="M2 5l10 8 10-8" fill="none" stroke="#06b394" stroke-width="1.8"/></svg>
        <span>stay@harbourretreats.com.au</span>
      </div>
      <div class="contact-row">
        <svg viewBox="0 0 24 24"><circle cx="12" cy="12" r="10" fill="#fff"/><path d="M2 12h20M12 2c3 3 3 17 0 20M12 2c-3 3-3 17 0 20" fill="none" stroke="#06b394" stroke-width="1.4"/></svg>
        <span>harbourretreats.com.au</span>
      </div>
    </div>

    <div class="services">
      <p>Our ‘Meet &amp; Greet’ service provides home owners with an increased level of Security and also allows us to:</p>
      <ul>
        <li><svg viewBox="0 0 15 12"><path d="M0 4h8V0l7 6-7 6V8H0z" fill="#06b394"/></svg><span>Prepare the home for their arrival<br>( lights, heaters, music etc.)</span></li>
        <li><svg viewBox="0 0 15 12"><path d="M0 4h8V0l7 6-7 6V8H0z" fill="#06b394"/></svg><span>Establish a rapport &amp;help facilitate<br>future bookings</span></li>
        <li><svg viewBox="0 0 15 12"><path d="M0 4h8V0l7 6-7 6V8H0z" fill="#06b394"/></svg><span>Reiterate their responsibilities to<br>ensure the return of their bond</span></li>
      </ul>
    </div>

    <div class="brand brand--back">HARBOUR<br>RETREATS</div>
  </section>
</body>
</html>
```